Mind Ledger - Web Design Project

We need a website for our new company based in Sao Paulo - Brazil. Our initial product is Mind Ledger - an online assessment system based on the most recent neuroscience academic research. The system gathers tests that are applied in the selection and evaluation of employees. We would like to see designs that use the colors black and blue. The final design should communicate trust. We like clean and simple designs.

Login to www.mindledger.com.br
login: user
pass: user

We need three pages:
1- Login page: http://www.mindledger.com.br/

2- Welcome page: http://www.mindledger.com.br/sys/admin/index.php

3- Results page: http://www.mindledger.com.br/sys/admin/admin_provas_resultados.php?unique_id=5

Our logo was created using ArtQuarry.
Next projetcs: Tests interface redesign.

Industry/Entity Type

It Company

Requirements
Must have
• Link folders. i.e.:
Home :: Users :: Paul Wren :: Test1
Nice to have
• Image Buttons
Should not have
• Noise

```html
<!DOCTYPE html>
<html lang="pt-BR">
<head>
<meta charset="utf-8">
<title>Mind Ledger — Login</title>
<link href="https://fonts.googleapis.com/css2?family=Oswald:wght@500&family=Arimo:wght@400;700&display=swap" rel="stylesheet">
<style>
  :root {
    --blue: #2070b8;
    --blue-dark: #1a5f9e;
    --ink: #111111;
    --brand-blue: #2a78c0;
    --white: #ffffff;
    --header-fade: #d9d9d9;
    --field-top: #c9c9c9;
    --field-bottom: #e6e6e6;
    --field-border: #a9b8c8;
    --button-text: #1f4f86;
    --footer: #060606;
  }
  * { margin: 0; padding: 0; box-sizing: border-box; }
  html, body { width: 1200px; height: 597px; overflow: hidden; }
  body {
    position: relative;
    font-family: "Arimo", Arial, sans-serif;
    background: var(--blue);
  }
  .site-header {
    position: absolute; left: 0; top: 0; width: 1200px; height: 110px;
    background: linear-gradient(to bottom, var(--white) 0%, var(--white) 55%, var(--header-fade) 100%);
    border-top: 1px solid #c8c8c8;
    z-index: 2;
  }
  .header-shadow {
    position: absolute; left: 200px; top: 104px; width: 816px; height: 12px;
    border-radius: 50%;
    box-shadow: 0 6px 10px rgba(0,0,0,0.45);
    z-index: 1;
  }
  .brand {
    position: absolute; left: 0; top: 0; width: 1200px; height: 110px;
    display: flex; align-items: center; justify-content: center; gap: 10px;
  }
  .brand-mark {
    width: 22px; height: 22px; border-radius: 50%;
    background: var(--brand-blue);
  }
  .brand-name {
    font-family: "Arimo", Arial, sans-serif;
    font-size: 30px; font-weight: 400; color: var(--ink);
    letter-spacing: -0.5px;
  }
  .login {
    position: absolute; left: 0; top: 0; width: 1200px; height: 597px;
  }
  .login-title {
    position: absolute; left: 521px; top: 180px;
    display: flex; align-items: center; gap: 7px;
  }
  .key-badge {
    width: 29px; height: 29px; border-radius: 50%;
    background: radial-gradient(circle at 40% 35%, #ffffff, #d4d4d4);
    display: flex; align-items: center; justify-content: center;
  }
  .login-title h1 {
    font-family: "Oswald", "Arial Narrow", sans-serif;
    font-weight: 500; font-size: 20px; color: var(--white);
    letter-spacing: -0.3px; line-height: 1;
  }
  .login-intro {
    position: absolute; left: 464px; top: 222px;
    font-size: 12px; color: #e8f0f8;
  }
  .field-label {
    position: absolute; left: 464px;
    font-size: 12px; color: #e8f0f8;
  }
  .field-label.email { top: 256px; }
  .field-label.password { top: 295px; left: 462px; }
  .field {
    position: absolute; left: 521px; width: 232px; height: 29px;
    border: 1px solid var(--field-border); border-radius: 3px;
    background: linear-gradient(to bottom, var(--field-top), var(--field-bottom));
    box-shadow: inset 0 1px 2px rgba(0,0,0,0.2);
  }
  .field.email { top: 249px; }
  .field.password { top: 288px; }
  .remember {
    position: absolute; left: 522px; top: 336px;
    display: flex; align-items: center; gap: 6px;
    font-size: 12px; color: #e8f0f8;
  }
  .checkbox {
    width: 10px; height: 10px; background: var(--white);
    border: 1px solid #555; display: flex; align-items: center; justify-content: center;
  }
  .submit {
    position: absolute; left: 663px; top: 334px; width: 89px; height: 29px;
    border: 1px solid #c9d3dd; border-radius: 2px;
    background: linear-gradient(to bottom, #ffffff 0%, #f1f1f1 50%, #d8d8d8 100%);
    font-family: "Oswald", "Arial Narrow", sans-serif; font-weight: 500;
    font-size: 16px; color: var(--button-text);
    display: flex; align-items: center; justify-content: center;
  }
  .site-footer {
    position: absolute; left: 0; top: 542px; width: 1200px; height: 55px;
    background: var(--footer);
    display: flex; align-items: center; justify-content: center;
    padding-top: 10px;
    font-size: 10.5px; font-weight: 700; color: var(--white);
  }
</style>
</head>
<body>
  <header class="site-header">
    <div class="brand">
      <span class="brand-mark"></span>
      <span class="brand-name">Mind Ledger</span>
    </div>
  </header>
  <div class="header-shadow"></div>

  <main class="login">
    <div class="login-title">
      <span class="key-badge">
        <svg width="16" height="16" viewBox="0 0 16 16" aria-hidden="true">
          <circle cx="10.5" cy="5.5" r="3.3" fill="none" stroke="#9a9a9a" stroke-width="1.8"/>
          <path d="M8 8 L2.5 13.5 M4 12 L5.5 13.5 M5.3 10.7 L6.8 12.2" stroke="#9a9a9a" stroke-width="1.8" stroke-linecap="round"/>
        </svg>
      </span>
      <h1>SEJA BEM-VINDO!</h1>
    </div>
    <p class="login-intro">Preencha os campos com seus dados para continuar:</p>

    <label class="field-label email">Email</label>
    <div class="field email"></div>
    <label class="field-label password">Senha</label>
    <div class="field password"></div>

    <div class="remember">
      <span class="checkbox">
        <svg width="9" height="9" viewBox="0 0 9 9" aria-hidden="true"><path d="M1 4.5 L3.5 7 L8 1.5" fill="none" stroke="#111" stroke-width="1.6"/></svg>
      </span>
      <span>Remember Me</span>
    </div>
    <div class="submit">ENTRAR</div>
  </main>

  <footer class="site-footer">© Copyrights 2013 Mind Ledger. All rights reserved</footer>
</body>
</html>
```